KRV Business Cards

We are a local commercial development company based in Silicon Valley and we would like a new business card. I've attached a copy of our company brochure to give a flavor of what we do, our logo, info company colors/graphics, and our current business card. We don't necessarily need a crazy makeover, but would like something that feels a little bit more "fresh" and modern (we've had the same business card design for 15+ years), but still in keeping with our overall brand -- clean, high-quality, modern but timeless. Would like to add our website to the info on the card (www.velmara.com) and would like the flexibility for some folks to have an efax number listed and some not to have that included (without it looking like there is a hole).

```html
<!DOCTYPE html>
<html lang="en">
<head>
<meta charset="utf-8">
<title>KRV Business Cards</title>
<link rel="stylesheet" href="https://fonts.googleapis.com/css2?family=Cinzel:wght@600&family=Crimson+Text:ital@1&family=Montserrat:ital,wght@0,400;0,500;1,400&display=swap">
<style>
  :root {
    --navy: #3a5068;
    --navy-text: #3d5470;
    --paper: #ebecee;
    --band: #c9cacc;
    --ink-light: #eef0f2;
    --stage: #d9d9d9;
  }
  * { box-sizing: border-box; margin: 0; padding: 0; }
  html, body { width: 1200px; height: 1006px; overflow: hidden; }
  body {
    background: var(--stage);
    display: flex; align-items: center; justify-content: center; gap: 40px;
  }
  .card {
    position: relative; width: 540px; height: 300px;
    background: var(--paper);
    box-shadow: 0 2px 8px rgba(0,0,0,.18);
    overflow: hidden;
  }
  .card__top { position: absolute; left: 0; top: 0; width: 100%; height: 182px; background: var(--navy); }
  .card__band { position: absolute; left: 0; top: 182px; width: 100%; height: 6px; background: var(--band); }
  .company {
    position: absolute; font-family: "Montserrat", sans-serif; font-weight: 500;
    color: var(--ink-light); text-transform: uppercase; letter-spacing: 2px; white-space: nowrap;
  }
  .company--front { left: 46px; top: 52px; font-size: 17px; }
  .company--back { left: 54px; top: 72px; font-size: 28px; letter-spacing: 3px; }
  .person { position: absolute; right: 44px; top: 108px; text-align: right; color: var(--ink-light); }
  .person__name { font-family: "Cinzel", serif; font-weight: 600; font-size: 18px; }
  .person__title { font-family: "Montserrat", sans-serif; font-style: italic; font-size: 12px; margin-top: 2px; }
  .contact {
    position: absolute; font-family: "Montserrat", sans-serif; font-size: 12.5px;
    color: var(--navy-text); list-style: none;
  }
  .contact li { display: flex; align-items: flex-start; gap: 10px; line-height: 1.35; margin-bottom: 5px; }
  .contact svg { width: 13px; height: 13px; flex: none; margin-top: 2px; fill: var(--navy-text); }
  .contact--left { left: 46px; top: 206px; }
  .contact--right { right: 40px; top: 228px; }
  .contact--right li { justify-content: flex-end; }
  .tagline {
    position: absolute; left: 56px; top: 236px;
    font-family: "Crimson Text", serif; font-style: italic; font-size: 16px; color: var(--navy-text);
  }
  .website {
    position: absolute; right: 54px; top: 240px;
    font-family: "Montserrat", sans-serif; font-weight: 500; font-size: 12px; letter-spacing: .5px; color: var(--navy-text);
  }
</style>
</head>
<body>
  <section class="card card--front">
    <div class="card__top"></div>
    <div class="card__band"></div>
    <div class="company company--front">KRV Development Co.</div>
    <div class="person">
      <div class="person__name">Dana L. Whitford</div>
      <div class="person__title">Partner</div>
    </div>
    <ul class="contact contact--left">
      <li><svg viewBox="0 0 24 24"><path d="M6.6 10.8a15.1 15.1 0 0 0 6.6 6.6l2.2-2.2a1 1 0 0 1 1-.25 11.4 11.4 0 0 0 3.6.57 1 1 0 0 1 1 1V20a1 1 0 0 1-1 1A17 17 0 0 1 3 4a1 1 0 0 1 1-1h3.5a1 1 0 0 1 1 1c0 1.25.2 2.450.57 3.6a1 1 0 0 1-.25 1z"/></svg>650.555.0148 (Direct)</li>
      <li><svg viewBox="0 0 24 24"><path d="M6.6 10.8a15.1 15.1 0 0 0 6.6 6.6l2.2-2.2a1 1 0 0 1 1-.25 11.4 11.4 0 0 0 3.6.57 1 1 0 0 1 1 1V20a1 1 0 0 1-1 1A17 17 0 0 1 3 4a1 1 0 0 1 1-1h3.5a1 1 0 0 1 1 1c0 1.25.2 2.45.57 3.6a1 1 0 0 1-.25 1z"/></svg>650.555.0190 (Main)</li>
      <li><svg viewBox="0 0 24 24"><path d="M12 2a7 7 0 0 0-7 7c0 5.2 7 13 7 13s7-7.8 7-13a7 7 0 0 0-7-7zm0 9.5A2.5 2.5 0 1 1 12 6.5a2.5 2.5 0 0 1 0 5z"/></svg>210 Linden Street, Alder Park<br>California 90210</li>
    </ul>
    <ul class="contact contact--right">
      <li>dana@velmara.com<svg viewBox="0 0 24 24"><path d="M2 5h20v14H2z M2 5l10 8 10-8" fill="none" stroke="#3d5470" stroke-width="2.2"/></svg></li>
      <li>www.velmara.com<svg viewBox="0 0 24 24"><circle cx="12" cy="12" r="9.5" fill="none" stroke="#3d5470" stroke-width="2.2"/><path d="M2.5 12h19M12 2.5c3 3 3 16 0 19M12 2.5c-3 3-3 16 0 19" fill="none" stroke="#3d5470" stroke-width="1.6"/></svg></li>
    </ul>
  </section>

  <section class="card card--back">
    <div class="card__top"></div>
    <div class="card__band"></div>
    <div class="company company--back">KRV Development Co.</div>
    <div class="tagline">Building Lasting Places for Business</div>
    <div class="website">www.velmara.com</div>
  </section>
</body>
</html>
```